NutriKeen children complimentary food package design

We need to design a bilingual (Arabic & English) baby complimentary powder food label, that is suitable for children from 1 to 10 years old. The primary purpose of this product is support healthy growth in general with special emphasis when the child is picky eater.
We want a design that is elegant, professional and western Looking. It will be printed onto a 400 grams can. The brand is called NutriKeen. The brand name is composed of two parts: "Nutri" which means advance and "Keen" which means ensured. The design should reflect this concept.
Be as creative as possible and we want the brands to have an classy, premium, elegant and professional feel, look and layout. Below are some requirements:
• Color theme: The general color is red keeping in mind that this product will be presented in different flavours: Vanilla, Chocolate and others.
• Unique ingredients/characteristics have to be mentioned on the front panel. Creative ideas are welcome and I am attaching illustrations from competitive products. The ingredients/characteristics are:
o DHA/AA
o 30 Vitamins & Minerals
o GMO free
• Although the brand name has a shield character, but we are looking to have a special character/emblem on the label that will be registered as a trademark. Creative ideas are welcome. Product images from other companies are attached as a reference. We are not limited to animal characters.
• The current organization of English and Arabic brand name is horizontal however this can be changes according to the designer discretion (e.g vertical).
Usually the label of infant formula can is divided into three parts: Left panel, Front panel and right Panel. Arabic text will be added later, just put a place holder and we will add it locally. We have no limitation for the number of colors. Usually the label has 4 process colors (CMYK) plus a number of spot colors and it is fine to use gold or silver color if deemed necessary for the label.
Updates
Target Market(s)
Children 1 - 10 years of age
Industry/Entity Type
Nutrition

```html
<!DOCTYPE html>
<html lang="en">
<head>
<meta charset="utf-8">
<title>NutriKeen Vanilla Label</title>
<link rel="stylesheet" href="https://fonts.googleapis.com/css2?family=Exo+2:wght@600&family=Cairo:wght@400;700&family=Alegreya:wght@700&family=Open+Sans:wght@400&display=swap">
<style>
  :root {
    --label-red: #ec1c24;
    --ribbon-red: #e21b23;
    --ribbon-shade: #b5121a;
    --gold: #b69858;
    --mist: #eceef0;
    --white: #ffffff;
    --page: #f4f4f4;
    --figure-grey: #a9abae;
  }
  html, body {
    margin: 0;
    padding: 0;
    width: 1200px;
    height: 1200px;
    overflow: hidden;
    background: var(--page);
  }
  .canvas {
    position: relative;
    width: 1200px;
    height: 1200px;
  }
  .label {
    position: absolute;
    left: 210px;
    top: 50px;
    width: 779px;
    height: 1100px;
    display: block;
  }
  .brand-latin { font-family: "Exo 2", sans-serif; font-weight: 600; fill: var(--white); }
  .brand-arabic { font-family: "Cairo", sans-serif; font-weight: 700; fill: var(--white); }
  .ribbon-text { font-family: "Alegreya", serif; font-weight: 700; fill: var(--white); }
  .age-latin { font-family: "Open Sans", sans-serif; fill: var(--white); }
  .age-arabic { font-family: "Cairo", sans-serif; font-weight: 700; fill: var(--white); }
  .claim-arabic { font-family: "Cairo", sans-serif; font-weight: 700; fill: var(--gold); }
  .claim-latin { font-family: "Alegreya", serif; font-weight: 700; fill: var(--gold); }
  .flavour-arabic { font-family: "Cairo", sans-serif; font-weight: 700; fill: var(--white); }
  .flavour-latin { font-family: "Open Sans", sans-serif; fill: var(--white); }
  .net-text { font-family: "Alegreya", serif; font-weight: 700; fill: var(--gold); }
  .net-arabic { font-family: "Cairo", sans-serif; fill: var(--gold); }
</style>
</head>
<body>
<div class="canvas">
  <svg class="label" viewBox="0 0 531 750" xmlns="http://www.w3.org/2000/svg">
    <rect class="label-base" width="531" height="750" fill="var(--label-red)"/>

    <path class="wave-light-upper" d="M0,330 C120,350 200,290 290,240 C370,195 470,205 531,300 V750 H0 Z" fill="var(--mist)"/>
    <path class="wave-gold" d="M0,340 C80,330 170,310 260,350 C340,385 440,310 531,300 V595 C450,560 380,480 300,430 C220,385 100,420 0,570 Z" fill="var(--gold)"/>
    <path class="wave-light-lower" d="M0,570 C100,420 220,385 300,430 C380,480 450,560 531,595 V750 H0 Z" fill="var(--mist)"/>
    <path class="wave-red-bottom" d="M0,605 C110,590 210,630 265,700 C300,748 420,745 531,610 V750 H0 Z" fill="var(--label-red)"/>

    <!-- brand block -->
    <circle class="brand-disc" cx="112" cy="99" r="64" fill="var(--white)"/>
    <text class="brand-arabic" x="485" y="98" font-size="50" text-anchor="end">نوتريكين</text>
    <text class="brand-latin" x="485" y="162" font-size="56" text-anchor="end">NutriKeen</text>

    <!-- feature ribbons -->
    <g class="ribbon ribbon-dha" transform="rotate(-2 360 241)">
      <polygon points="455,222 486,226 470,238 484,252 455,258" fill="var(--ribbon-shade)"/>
      <polygon points="275,221 460,221 460,261 275,261 286,241" fill="var(--ribbon-red)"/>
      <text class="ribbon-text" x="362" y="251" font-size="24" text-anchor="middle">DHA/AA</text>
    </g>
    <g class="ribbon ribbon-vitamins" transform="rotate(4 360 308)">
      <polygon points="238,288 482,288 472,308 482,328 238,328 248,308" fill="var(--ribbon-red)"/>
      <text class="ribbon-text" x="360" y="316" font-size="20" text-anchor="middle">30 Vitamins &amp; Minerals</text>
    </g>
    <g class="ribbon ribbon-gmo" transform="rotate(-2 363 373)">
      <polygon points="258,380 290,384 276,394 290,404 262,404" fill="var(--ribbon-shade)"/>
      <polygon points="282,354 440,354 430,373 440,392 282,392" fill="var(--ribbon-red)"/>
      <text class="ribbon-text" x="362" y="381" font-size="21" text-anchor="middle">GMO free</text>
    </g>

    <!-- age statement -->
    <g class="age-line" transform="rotate(29 140 380)">
      <text class="age-arabic" x="150" y="362" font-size="15" text-anchor="start">للأطفال من عمر سنة حتى ١٠ سنوات</text>
      <text class="age-latin" x="140" y="384" font-size="22">For children 1-10 years</text>
    </g>

    <!-- mascot area -->
    <rect class="mascot" x="30" y="458" width="220" height="152" rx="30" fill="var(--figure-grey)" opacity="0.55" role="img" aria-label="Mascot character: a grey shield with a red cape and legs"/>

    <!-- children silhouettes -->
    <rect class="children" x="385" y="397" width="130" height="155" rx="20" fill="var(--white)" opacity="0.85" role="img" aria-label="White silhouettes of a small child and a school child with a backpack"/>

    <!-- nutrition claim -->
    <g class="claim" transform="rotate(6 360 615)">
      <text class="claim-arabic" x="360" y="612" font-size="21" text-anchor="middle">غذاء تكميلي متوازن</text>
      <text class="claim-latin" x="360" y="632" font-size="13" text-anchor="middle">complete and balanced nutrition</text>
    </g>

    <!-- flavour -->
    <text class="flavour-arabic" x="93" y="690" font-size="38" text-anchor="middle">فانيلا</text>
    <text class="flavour-latin" x="95" y="727" font-size="34" text-anchor="middle">Vanilla</text>

    <!-- serving visual -->
    <circle class="serving-ring" cx="246" cy="687" r="56" fill="var(--label-red)"/>
    <circle class="serving" cx="246" cy="687" r="50" fill="var(--mist)" stroke="var(--white)" stroke-width="3" role="img" aria-label="Glass of vanilla milk with vanilla flowers"/>

    <!-- net weight -->
    <text class="net-arabic" x="425" y="686" font-size="11" text-anchor="end">٤٠٠ غرام صافي</text>
    <text class="net-text" x="330" y="709" font-size="15">℮ NET 400g</text>
  </svg>
</div>
</body>
</html>
```